Signage setout with photos for side of Mowing Trailer

We need signage for our mowing trailer to attract new business.
Specifically a Rear sign 1470x880mm and Side signs 2400x880mm
Sign needs to be modern and professional.
Some example uploads as to what we have thought about so far.
Logo doesn't need to be the green colour.
Logo words and Logo of Mower do not need to be together.
Link to get a mower image>
https://brightfieldgear.example/tandem
Updates

Need extra days to review

Target Market(s)

Other Customers driving past the trailer.

Industry/Entity Type

Lawnmowing / Landscaping

Requirements
Must have
• Phone Number, Company Name & Logo, Web address, Chatterlane and Pixo Logos, Comment - "Acreage & Commercial Specialists" Catchcry - "100% Electric Mowing Company - est 2017" Services "Mowing, Hedging, Pressure Cleaning, Weed Control, Fencing, Turfing, Mulching and Rubbish Removal"
Nice to have
• Full colour background images.

```html
<!DOCTYPE html>
<html lang="en">
<head>
<meta charset="utf-8">
<title>Fresh Field Mowing – Trailer Signage</title>
<link rel="stylesheet" href="https://fonts.googleapis.com/css2?family=Montserrat:wght@600;700&family=Yellowtail&display=swap">
<style>
  :root {
    --orange: #ec6a2a;
    --white: #ffffff;
    --grass-dark: #2f8a2c;
    --grass-mid: #4ba53a;
    --grass-light: #7cc35a;
    --canvas: #ffffff;
  }
  * { box-sizing: border-box; margin: 0; padding: 0; }
  html, body {
    width: 1200px; height: 870px; overflow: hidden;
    background: var(--canvas);
    font-family: "Montserrat", Arial, sans-serif;
  }
  .sign {
    position: absolute;
    overflow: hidden;
    box-shadow: 6px 7px 7px rgba(0,0,0,.35);
  }
  .sign-side { left: 106px; top: 58px; width: 996px; height: 364px; }
  .sign-rear { left: 296px; top: 451px; width: 610px; height: 363px; }

  .grass-photo {
    position: absolute; inset: 0;
    background:
      radial-gradient(ellipse at 55% 60%, rgba(140,205,100,.55), transparent 60%),
      radial-gradient(ellipse at 10% 20%, rgba(40,120,40,.6), transparent 55%),
      linear-gradient(180deg, var(--grass-mid) 0%, var(--grass-dark) 45%, var(--grass-mid) 100%);
  }
  .layer { position: absolute; }

  /* Side sign */
  .side-brand {
    left: 22px; top: 16px; height: 46px;
    display: flex; align-items: center; gap: 10px;
    color: var(--white); font-weight: 700; font-size: 18px; line-height: 1.05;
    text-transform: uppercase;
  }
  .brand-dot { width: 38px; height: 38px; border-radius: 50%; background: var(--white); flex: none; }
  .side-divider { left: 268px; top: 12px; width: 2px; height: 54px; background: var(--white); }
  .side-web {
    left: 286px; top: 20px; height: 38px; line-height: 38px;
    color: var(--white); font-weight: 700; font-size: 26px; letter-spacing: 3px;
  }
  .social { display: flex; gap: 10px; }
  .social span { width: 36px; height: 36px; border-radius: 50%; background: var(--orange); display: block; }
  .side-social { left: 880px; top: 21px; }

  .band-white { background: var(--white); left: 0; width: 100%; }
  .side-band { top: 78px; height: 60px; }
  .side-headline {
    top: 78px; left: 0; width: 100%; height: 60px; line-height: 60px;
    text-align: center; color: var(--orange); font-weight: 700; font-size: 40px; letter-spacing: .5px;
  }
  .side-catchcry {
    top: 148px; left: 0; width: 100%; text-align: center;
    font-family: "Yellowtail", cursive; color: var(--orange); font-size: 38px; line-height: 44px;
  }
  .services {
    list-style: none; color: var(--white); font-weight: 700; font-size: 18px;
    text-transform: uppercase; letter-spacing: .3px;
  }
  .services li { position: absolute; white-space: nowrap; }
  .services li::before { content: "• "; }
  .phone-bar {
    background: var(--orange); color: var(--white); border-radius: 16px 16px 0 0;
    display: flex; align-items: center; justify-content: center; font-weight: 700;
  }
  .side-phone { left: 128px; top: 299px; width: 732px; height: 65px; gap: 14px; }
  .side-phone .call { font-size: 38px; font-weight: 600; }
  .side-phone .number { font-size: 56px; letter-spacing: 4px; }

  /* Rear sign */
  .rear-brand {
    left: 0; top: 24px; width: 100%;
    display: flex; align-items: center; justify-content: center; gap: 14px;
    color: var(--orange); font-weight: 700; font-size: 30px; text-transform: uppercase;
  }
  .rear-brand .brand-dot { background: var(--orange); width: 44px; height: 44px; }
  .rear-rule { left: 85px; top: 110px; width: 439px; border-top: 2px dashed var(--white); }
  .rear-headline {
    top: 124px; left: 0; width: 100%; text-align: center;
    color: var(--white); font-weight: 700; font-size: 36px; line-height: 46px;
  }
  .rear-band { top: 227px; height: 52px; }
  .rear-web {
    left: 16px; top: 227px; height: 52px; line-height: 52px;
    color: var(--orange); font-weight: 700; font-size: 24px; letter-spacing: 2.5px;
  }
  .rear-social { left: 522px; top: 236px; gap: 8px; }
  .rear-social span { width: 32px; height: 32px; }
  .rear-phone { left: 61px; top: 299px; width: 486px; height: 64px; }
  .rear-phone .number { font-size: 58px; letter-spacing: 4px; }
</style>
</head>
<body>

<section class="sign sign-side">
  <div class="grass-photo" role="img" aria-label="Close-up photo of green grass blades"></div>
  <div class="layer side-brand"><span class="brand-dot"></span><span>Fresh Field<br>Mowing</span></div>
  <div class="layer side-divider"></div>
  <div class="layer side-web">WWW.FRESHFIELDMOWING.AU</div>
  <div class="layer social side-social"><span aria-label="Chatterlane"></span><span aria-label="Pixo"></span></div>
  <div class="layer band-white side-band"></div>
  <h1 class="layer side-headline">ACREAGE &amp; COMMERCIAL SPECIALISTS</h1>
  <p class="layer side-catchcry">100% Electric Mowing Company Est 2017</p>
  <ul class="layer services" style="left:0;top:0;">
    <li style="left:68px;top:214px">Mowing</li>
    <li style="left:216px;top:214px">Pressure Cleaning</li>
    <li style="left:516px;top:214px">Fencing</li>
    <li style="left:677px;top:214px">Mulching</li>
    <li style="left:68px;top:249px">Hedging</li>
    <li style="left:216px;top:249px">Weed Control</li>
    <li style="left:516px;top:249px">Turfing</li>
    <li style="left:677px;top:249px">Rubbish Removal</li>
  </ul>
  <div class="layer phone-bar side-phone"><span class="call">CALL US :</span><span class="number">3555 0142</span></div>
</section>

<section class="sign sign-rear">
  <div class="grass-photo" role="img" aria-label="Close-up photo of green grass blades"></div>
  <div class="layer rear-brand"><span class="brand-dot"></span><span>Fresh Field Mowing</span></div>
  <div class="layer rear-rule"></div>
  <h2 class="layer rear-headline">ACREAGE &amp; COMMERCIAL<br>SPECIALISTS</h2>
  <div class="layer band-white rear-band"></div>
  <div class="layer rear-web">WWW.FRESHFIELDMOWING.AU</div>
  <div class="layer social rear-social"><span aria-label="Chatterlane"></span><span aria-label="Pixo"></span></div>
  <div class="layer phone-bar rear-phone"><span class="number">3555 0142</span></div>
</section>

</body>
</html>
```